Tails of Comfort Therapy & Dog Training

I have a dual themed business. I am a nationally recognized dog trainer for NHF (National Hound Federation) and Animal Allies (Pet Therapy). One side of my business card will need to address my pet therapy ministry called "Tails of Comfort Therapy". We visit almost 1,000 people a month bringing emotionally uplifting happy visits for nursing homes, veterans hospitals, hospice care, surgery recovery, school systems, and libraries, etc. In addition to emotionally positive effects, pet therapy also helps with anxiety, mobility, regulating blood pressure, and many more advantages. I've attached 2 graphics that are connected with this ministry; #1 paw print inside ribbon heart, #2 clasping hands sketch. The story behind the clasping hands is that it is an actual picture of my hand holding my mother's hand on her death bed (with a sketch filter used). My mother lived in a different state than I live in, and I had wished she had pet therapy available to her in her last months of life. They would have provided some bright moments to her difficult days. So, I vowed that although I was not able to help my own mother, I could train my own dog to reach out to hundreds of people in the community I live in. I have continued to live up to that vow, and have gone on to become a national trainer for other people who would like to train their pets to do the same thing.SIDE TWO of my business card will be announcing that I am a dog trainer for puppies, basic obedience, pet therapy, ESA (emotional support animals), and service dogs. Additionally, I offer canine body language training, dog agility training, and cognitive training. I have also attached two graphics for this side: #1 NHF logo, #2 Animal Allies Evaluation

Target Market(s)

Industry/Entity Type

Dog Training

Contact Information for Business Card

I'm looking for a designer who is good with color scheme & fonts.
2-sided card
one side for pet therapy
one side for dog training

Logo Text

Tails of ComfortTherapy

Font styles to use
Sans Serif
Decorative

Colors

Designer to choose colors to be used in the design.

Requirements
Must have
• -Contact information: Marla Quince (555) 203-9164
• - Contact information for online: Tails of Comfort Therapy (Facebook, Instagram & Twitter)
• - Graphics for pet therapy: clasping hands
• - Graphics for dog training: NHF Model Neighbor Dog, Animal Allies
• - List of dog training classes I offer: Basic Obedience, NHF Model Neighbor Dog, NHF B.R.I.G.H.T. Pup, Pet Therapy training, ESA (Emotional Support Animal), Service Dog training, Canine Body Language, Dog Agility, Cognitive Training, Dog Trick Training
Nice to have
• appealing graphic for dog training school
• Titles in decorative font (but still easy to read) & detail info in very easy to read font

```html
<!DOCTYPE html>
<html lang="en">
<head>
<meta charset="utf-8">
<title>Tails of Comfort Therapy – Business Card</title>
<link href="https://fonts.googleapis.com/css2?family=Oswald:wght@500&family=Open+Sans:wght@400;600;700&family=Great+Vibes&display=swap" rel="stylesheet">
<style>
  :root {
    --bg: #e9e6e1;
    --card-yellow: #f1e236;
    --ink: #1c1c1c;
    --brand-blue: #2b5eb3;
    --sketch-light: #e9ddc6;
    --sketch-mid: #b8a58a;
    --sleeve: #3a2a22;
    --badge-blue: #2a58a8;
    --badge-pink: #c0264f;
  }
  * { box-sizing: border-box; margin: 0; padding: 0; }
  html, body { width: 1200px; height: 1200px; overflow: hidden; }
  body {
    background: var(--bg);
    font-family: "Open Sans", Arial, sans-serif;
    color: var(--ink);
    position: relative;
  }
  .card {
    position: absolute;
    top: 198px;
    width: 460px;
    height: 805px;
    background: var(--card-yellow);
    box-shadow: 0 6px 18px rgba(0,0,0,.18);
    overflow: hidden;
  }
  .card--training { left: 110px; }
  .card--therapy { left: 630px; }

  /* Training side */
  .contact {
    position: absolute;
    top: 48px;
    right: 40px;
    text-align: right;
  }
  .contact__name {
    font-family: "Oswald", "Arial Narrow", sans-serif;
    font-weight: 500;
    font-size: 40px;
    letter-spacing: 1px;
    line-height: 1;
    text-transform: uppercase;
  }
  .contact__role {
    color: var(--brand-blue);
    font-size: 18px;
    letter-spacing: .5px;
    margin-top: 4px;
    padding-right: 30px;
  }
  .contact__line {
    display: flex;
    justify-content: flex-end;
    align-items: center;
    gap: 10px;
    font-size: 18px;
    margin-top: 6px;
  }
  .contact__line svg { width: 18px; height: 18px; flex: none; }
  .services {
    position: absolute;
    left: 40px;
    top: 470px;
    width: 290px;
  }
  .services__title {
    color: var(--brand-blue);
    font-weight: 700;
    font-size: 20px;
    letter-spacing: 1px;
    margin-bottom: 8px;
  }
  .services__list { list-style: none; font-size: 18px; line-height: 1.45; }
  .services__list .is-accent { color: var(--brand-blue); }
  .credentials {
    position: absolute;
    right: 40px;
    top: 490px;
    display: flex;
    flex-direction: column;
    align-items: center;
    gap: 18px;
  }
  .badge-seal { width: 64px; height: 64px; border-radius: 50%; background: var(--badge-blue); }
  .partner-mark { display: flex; align-items: center; gap: 6px; }
  .partner-mark__dot { width: 26px; height: 26px; border-radius: 50%; background: var(--badge-pink); }
  .partner-mark__name { font-weight: 700; font-size: 17px; color: var(--badge-pink); }

  /* Therapy side */
  .therapy-title {
    font-family: "Great Vibes", cursive;
    color: var(--brand-blue);
    font-size: 48px;
    text-align: center;
    margin-top: 40px;
    line-height: 1;
  }
  .find-us {
    text-align: center;
    margin-top: 34px;
    font-size: 17px;
  }
  .find-us__label { font-weight: 700; font-size: 15px; margin-bottom: 4px; }
  .find-us__item {
    display: flex;
    justify-content: center;
    align-items: center;
    gap: 6px;
    line-height: 1.4;
  }
  .find-us__icon { width: 11px; height: 11px; background: var(--brand-blue); }
  .hands-art {
    position: absolute;
    left: 60px;
    bottom: 0;
    width: 400px;
    height: 500px;
  }
</style>
</head>
<body>

<section class="card card--training">
  <div class="contact">
    <h1 class="contact__name">Marla Quince</h1>
    <p class="contact__role">DOG TRAINER</p>
    <p class="contact__line">(555) 203-9164
      <svg viewBox="0 0 24 24" aria-hidden="true"><path d="M6.6 10.8a15 15 0 0 0 6.6 6.6l2.2-2.2a1 1 0 0 1 1-.25 11.4 11.4 0 0 0 3.6.6 1 1 0 0 1 1 1V20a1 1 0 0 1-1 1A17 17 0 0 1 3 4a1 1 0 0 1 1-1h3.5a1 1 0 0 1 1 1 11.4 11.4 0 0 0 .6 3.6 1 1 0 0 1-.25 1z" fill="var(--brand-blue)"/></svg>
    </p>
    <p class="contact__line">tailsofcomforttherapy@kennelpost.net
      <svg viewBox="0 0 24 24" aria-hidden="true"><rect x="2" y="5" width="20" height="14" fill="none" stroke="var(--brand-blue)" stroke-width="2"/><path d="M2 5l10 8 10-8" fill="none" stroke="var(--brand-blue)" stroke-width="2"/></svg>
    </p>
  </div>

  <div class="services">
    <h2 class="services__title">WE PROVIDE :</h2>
    <ul class="services__list">
      <li>Basic Obedience,</li>
      <li>NHF Model Neighbor Dog,</li>
      <li class="is-accent">NHF B.R.I.G.H.T. Pup,</li>
      <li class="is-accent">Pet Therapy training</li>
      <li>ESA (Emotional Support Animal),</li>
      <li>Canine Body Language,</li>
      <li class="is-accent">Service Dog training,</li>
      <li class="is-accent">Canine Body Language,</li>
      <li>Dog Agility, Cognitive Training,</li>
      <li>Dog Trick Training</li>
    </ul>
  </div>

  <div class="credentials">
    <div class="badge-seal" role="img" aria-label="Evaluator certification badge"></div>
    <div class="partner-mark">
      <span class="partner-mark__dot"></span>
      <span class="partner-mark__name">Animal Allies</span>
    </div>
  </div>
</section>

<section class="card card--therapy">
  <h2 class="therapy-title">Tails of Comfort Therapy</h2>
  <div class="find-us">
    <p class="find-us__label">FIND US :</p>
    <p class="find-us__item"><span class="find-us__icon"></span>TailsOfComfortTherapy</p>
    <p class="find-us__item"><span class="find-us__icon"></span>@TailsofComfrt</p>
    <p class="find-us__item"><span class="find-us__icon"></span>@TailsofComfrt</p>
  </div>
  <svg class="hands-art" viewBox="0 0 400 500" role="img" aria-label="Sketch illustration of two clasped hands with a sleeve bearing a paw print inside a ribbon heart">
    <defs>
      <linearGradient id="handsTone" x1="0" y1="0" x2="1" y2="1">
        <stop offset="0" stop-color="var(--sketch-light)"/>
        <stop offset="1" stop-color="var(--sketch-mid)"/>
      </linearGradient>
    </defs>
    <rect x="0" y="0" width="400" height="500" fill="url(#handsTone)"/>
  </svg>
</section>

</body>
</html>
```